Flyer for the Harvest Lantern Gathering 2018

Design a flyer for our annual conference with basic information about the conference: conference logo and year,

Location:
Dunmore Community Center (Downtown Portland)
482 Willowby Street, Portland, ME 04117,

Date:
August 24th, 25th and 26th, 2018
Start time 6:00PM

I would like the following three words added to the flyer. These words describe the vision of the conference:
Prophetic, Worship, Prayer

```html
<!DOCTYPE html>
<html lang="en">
<head>
<meta charset="utf-8">
<title>Harvest Lantern Gathering 2018</title>
<link rel="stylesheet" href="https://fonts.googleapis.com/css2?family=Montserrat:wght@700;800;900&family=Open+Sans:wght@400;700&display=swap">
<style>
  :root {
    --ink: #141414;
    --navy: #2e2b70;
    --violet: #6a2d8f;
    --magenta: #a2236f;
    --white: #ffffff;
    --gold: #e8a91c;
    --smoke: #d9dadb;
  }
  * { margin: 0; padding: 0; box-sizing: border-box; }
  html, body { width: 849px; height: 1200px; overflow: hidden; background: var(--white); }
  .flyer {
    position: relative;
    width: 849px;
    height: 1200px;
    overflow: hidden;
    font-family: "Open Sans", Arial, sans-serif;
  }
  .backdrop {
    position: absolute; inset: 0;
    background:
      radial-gradient(ellipse 330px 120px at 440px 640px, #c8124f 0%, rgba(200,18,79,0.85) 55%, rgba(200,18,79,0) 100%),
      linear-gradient(180deg, #f3f3f1 0%, #f7f3d8 14%, #f4e24a 30%, #ecd62a 42%, #d9c63a 50%, #3a3530 64%, #121212 76%, #3a3b3d 88%, #6f7072 100%);
  }
  .worshippers {
    position: absolute;
    left: 190px; top: 498px;
    width: 520px; height: 282px;
    background: linear-gradient(180deg, #6b2f8e 0%, #5f2a85 100%);
    border-radius: 120px 120px 20px 20px;
    opacity: 0.92;
  }
  .event-title {
    position: absolute; top: 22px; width: 100%;
    text-align: center;
    font-family: "Montserrat", Arial, sans-serif;
    font-weight: 800;
    font-size: 62px;
    letter-spacing: 1px;
    color: var(--ink);
  }
  .event-subtitle {
    position: absolute; top: 100px; width: 100%;
    text-align: center;
    font-family: "Montserrat", Arial, sans-serif;
    font-weight: 800;
    font-size: 25px;
    color: var(--ink);
  }
  .vision {
    position: absolute; top: 168px; width: 100%;
    text-align: center;
    font-family: "Montserrat", Arial, sans-serif;
    font-weight: 900;
    font-size: 84px;
    line-height: 86px;
    text-shadow: 3px 4px 6px rgba(0,0,0,0.35);
  }
  .vision .prophetic { color: var(--navy); display: block; }
  .vision .worship { color: var(--violet); display: block; }
  .vision .prayer { color: var(--magenta); display: block; }
  .date-frame { position: absolute; left: 0; top: 0; }
  .event-when {
    position: absolute; top: 656px; width: 100%;
    text-align: center;
    font-weight: 700;
    font-size: 34px;
    line-height: 56px;
    color: var(--white);
  }
  .venue {
    position: absolute; top: 818px; width: 100%;
    text-align: center;
    color: var(--white);
  }
  .venue-name { font-weight: 700; font-size: 33px; line-height: 44px; }
  .venue-area { font-size: 24px; line-height: 34px; }
  .venue-address { font-size: 26px; line-height: 38px; }
  .brand-mark {
    position: absolute; left: 361px; top: 1010px;
    width: 128px; height: 128px;
    border-radius: 50%;
    border: 4px solid var(--gold);
  }
  .brand-name {
    position: absolute; top: 1140px; width: 100%;
    text-align: center;
    font-family: "Montserrat", Arial, sans-serif;
    font-weight: 800;
    font-size: 44px;
    letter-spacing: 4px;
    color: var(--ink);
  }
</style>
</head>
<body>
<main class="flyer">
  <div class="backdrop" role="img" aria-label="Swirling ink in white, yellow, crimson and black smoke"></div>
  <div class="worshippers" role="img" aria-label="Purple silhouettes of worshippers with raised arms"></div>

  <h1 class="event-title">HALGA 2018</h1>
  <p class="event-subtitle">HARVEST LANTERN GATHERING</p>

  <h2 class="vision">
    <span class="prophetic">PROPHETIC,</span>
    <span class="worship">WORSHIP,</span>
    <span class="prayer">PRAYER</span>
  </h2>

  <svg class="date-frame" width="849" height="1200" viewBox="0 0 849 1200" aria-hidden="true">
    <path d="M122 633 H762 Q778 633 778 649 V690" fill="none" stroke="#fff" stroke-width="4"/>
    <path d="M76 700 V760 Q76 776 92 776 H742" fill="none" stroke="#fff" stroke-width="4"/>
  </svg>

  <p class="event-when">August 24th, 25th &amp; 26th, 2018<br>6:00PM</p>

  <address class="venue" style="font-style: normal;">
    <div class="venue-name">Dunmore Community Center</div>
    <div class="venue-area">(Downtown Portland)</div>
    <div class="venue-address">482 Willowby Street, Portland, ME 04117,</div>
  </address>

  <div class="brand-mark"></div>
  <p class="brand-name">HALGA</p>
</main>
</body>
</html>
```